Real Estate Company Needs Stationery Design Project, Logo Redesign, For Sale Design

We are a real estate company in San Diego California. We handle mostly coastal areas with middle to high end properties. Our colors are gray, dark silver, and black. I do not want anything Cartoon-ish but it does need to have a modern feel. We are looking to have these items below designed. We have a logo that we like and we have already built some name recognition so I don’t want to change the design but I am open to it… so feel free to pitch a new logo if you would like. We do however need our logo designed by a pro and put into high resolution Illustrator file. We listed the items we need designed below 1-4 with a description of what we are looking for below that. We need items 1-4 done with item 5 being optional for you designers. I attached our logo, current business cards, and a picture of real estate for sale sings for reference. Please feel free to email us if you have an questions.

Needs:
1) Logo Redesign.
- I Attached the Logo. I made this logo and need it to be done by a pro.
- I need my logo to be done in high resolution and an illustrator file
- I also need a copy of the logo to fit as my Friendloop background: 851 Wide by 315px Tall

2) Business Cards
- I need business cards design in an illustrator file.
- I need cards designed once with a space for a personal photo and one designed without a personal photo. Personal Photo = A picture of the agent or person.

3) Real Estate For sale signs Designed.
- I need these signs to fit 24”x18”
- Do not say For Sale on them, just have info as listed below
- I would like one design with a space for a personal picture of me, and one designed without a space for a picture
- Need this in an illustrator file

4) Stationary items

5) Some optional items that we could use are:
- Email Signature
- Newsletter template design
- Background design for Chirplet page
- Header and footer. One without contact info and one with contact info
For sale Signs Need: Logo, My Name, 888 #, website.
I do not want them to say “For Sale” on them. I attached a picture of some example signs. I also wouldn’t mind for it to say something in small writing along the lines of “View this home at –or- view details of this home at: CoastlineHomeFinder.example”

Cards need: Logo, Name, Serving All San Diego County, Cell #, Office/Fax#, Email, Website, DRE Lic#.
Backside should have either Logo or say something like “Referrals are the largest complements we can get…” Basically be creative, we could even use it to list all of our social media platforms: Friendloop, Chirplet, Website, Vidstream, Cirqle+.

What to Avoid: Comic / Cartoonish look, but needs to be modern and smooth.

Marcus Tillwater
The Tillwater Group
Real Estate Sales & Investments
Covering All San Diego County “Optional”
Cell: 760-555-0139
Office/Fax 888-555-0162
Marcus@TillwaterGroup.example
www.CoastlineHomeFinder.example
DRE#07392054

Social Media:
http://www.facebook.com/TillwaterGroup
http://www.youtube.com/TillwaterGroup
http://www.yelp.com/biz/the-tillwater-group-oceanside-2

Find us on:
Homevista.example
Parcelly.example
Listingbay.example
Cirqle+
Careernet.example

Target Market(s)

San Diego California Real Estate.

Industry/Entity Type

Real Estate

Requirements
Must have
• 1) Logo Redesign.

2) Business Cards

4) Stationary items
Nice to have
• 5) Some optional items that we could use are:
- Email Signature
Should not have
• Cartoon look.

```html
<!DOCTYPE html>
<html lang="en">
<head>
<meta charset="utf-8">
<title>The Tillwater Group — Yard Sign</title>
<link rel="stylesheet" href="https://fonts.googleapis.com/css2?family=Montserrat:wght@400;600&display=swap">
<style>
  :root {
    --backdrop-center: #2b2b2b;
    --backdrop-edge: #0d0d0d;
    --silver-dark: #b9b9bb;
    --silver-mid: #d6d6d8;
    --silver-light: #f1f1f2;
    --ink: #141414;
    --panel-top: #1a1515;
    --panel-bottom: #070606;
    --white: #ffffff;
  }
  * { margin: 0; padding: 0; box-sizing: border-box; }
  html, body { width: 1200px; height: 1000px; overflow: hidden; }
  body {
    position: relative;
    background: radial-gradient(ellipse at 50% 55%, var(--backdrop-center) 0%, var(--backdrop-edge) 80%);
    font-family: "Montserrat", sans-serif;
  }
  .sign {
    position: absolute;
    left: 161px; top: 161px;
    width: 890px; height: 668px;
  }
  .brand-panel {
    position: absolute; left: 0; top: 0;
    width: 890px; height: 292px;
    background: linear-gradient(100deg, var(--silver-dark) 0%, var(--silver-mid) 30%, var(--silver-light) 62%, var(--silver-mid) 80%, var(--silver-dark) 100%);
    text-align: center;
  }
  .brand-mark {
    position: absolute; left: 417px; top: 38px;
    width: 56px; height: 56px;
    background: var(--ink);
  }
  .brand-name {
    position: absolute; left: 0; right: 0; top: 120px;
    font-weight: 600;
    font-size: 56px;
    letter-spacing: 1px;
    color: var(--ink);
    line-height: 1;
  }
  .brand-tagline {
    position: absolute; left: 0; right: 0; top: 222px;
    font-weight: 600;
    font-size: 18px;
    letter-spacing: 3px;
    text-transform: uppercase;
    color: var(--ink);
    line-height: 1;
  }
  .divider-band {
    position: absolute; left: 0; top: 292px;
    width: 890px; height: 18px;
    background: linear-gradient(90deg, #5e5e5e 0%, #9c9c9c 20%, #f4f4f4 50%, #a8a8a8 78%, #6a6a6a 100%);
  }
  .contact-panel {
    position: absolute; left: 0; top: 310px;
    width: 890px; height: 358px;
    background: linear-gradient(180deg, var(--panel-top) 0%, var(--panel-bottom) 100%);
    color: var(--white);
    text-align: center;
  }
  .agent-name {
    position: absolute; left: 0; right: 0; top: 34px;
    font-weight: 600;
    font-size: 58px;
    letter-spacing: 3px;
    line-height: 1;
  }
  .agent-license {
    position: absolute; left: 0; right: 0; top: 106px;
    font-size: 14px;
    letter-spacing: 1px;
    line-height: 1;
  }
  .agent-phone {
    position: absolute; left: 0; right: 0; top: 152px;
    font-weight: 400;
    font-size: 92px;
    letter-spacing: 2px;
    line-height: 1;
  }
  .agent-website {
    position: absolute; left: 0; right: 0; top: 280px;
    font-weight: 400;
    font-size: 38px;
    letter-spacing: 1.5px;
    line-height: 1;
  }
</style>
</head>
<body>
  <div class="sign">
    <div class="brand-panel">
      <div class="brand-mark" role="img" aria-label="Company logo mark"></div>
      <div class="brand-name">The Tillwater Group</div>
      <div class="brand-tagline">Real Estate Sales &amp; Investments</div>
    </div>
    <div class="divider-band"></div>
    <div class="contact-panel">
      <div class="agent-name">Marcus Tillwater</div>
      <div class="agent-license">DRE#07392054</div>
      <div class="agent-phone">888 555 0162</div>
      <div class="agent-website">www.CoastlineHomeFinder.example</div>
    </div>
  </div>
</body>
</html>
```